Modern wordpress-enabled design wanted for translations agency serving large corporations

We are a translation agency and we only work for corporate clients and not private individuals. We are currently using the Larvesk wordpress theme and an upload feature called trobanex. It is important that prospective clients can upload their file. So we need a cool design for that kind of feature. We offer different kinds of translations tailored to the needs or global corporations. Corporate communications translations, legal translations, financial translations, healthcare translations, financial translations, audit translations.

```html
<!DOCTYPE html>
<html lang="en">
<head>
<meta charset="utf-8">
<title>Trobanex Translations</title>
<link href="https://fonts.googleapis.com/css2?family=Open+Sans:wght@300;400;600;700;800&display=swap" rel="stylesheet">
<style>
:root{
  --orange:#f26522;
  --ink:#333333;
  --muted:#8a8a8a;
  --line:#e2e2e2;
  --band:#ededed;
  --white:#ffffff;
  --hero-a:#5a5450;
  --hero-b:#2e2a28;
  --partner-red:#c8102e;
  --partner-blue:#1b3f8f;
  --partner-grey:#5b7fa8;
}
*{box-sizing:border-box;margin:0;padding:0}
html,body{width:1200px;height:2280px;overflow:hidden}
body{position:relative;background:var(--white);font-family:'Open Sans',Arial,sans-serif;color:var(--ink)}
.section{position:absolute;left:0;width:1200px}

/* header */
.site-header{top:0;height:90px;background:var(--white)}
.brand{position:absolute;left:72px;top:14px}
.brand-name{font-size:34px;font-weight:800;letter-spacing:1px;line-height:34px;color:var(--ink)}
.brand-sub{display:flex;align-items:center;gap:8px;font-size:20px;font-weight:700;letter-spacing:2px;color:var(--ink);margin-top:2px}
.brand-sub .dot{width:14px;height:14px;background:var(--orange)}
.nav{position:absolute;left:440px;top:58px;display:flex}
.nav a{font-size:13px;font-weight:600;color:var(--ink);text-decoration:none;padding:0 26px;border-right:1px solid var(--line);text-transform:uppercase}
.nav a.active{color:var(--orange)}
.nav a:last-child{border-right:none}
.header-actions{position:absolute;right:70px;top:16px;display:flex;gap:12px}
.btn{display:inline-flex;align-items:center;gap:6px;background:var(--orange);color:var(--white);font-size:12px;font-weight:700;text-transform:uppercase;padding:8px 16px;line-height:16px}

/* hero */
.hero{top:90px;height:470px;background:linear-gradient(180deg,var(--hero-a),var(--hero-b))}
.hero-photo{position:absolute;inset:0;background:linear-gradient(90deg,#6b625c 0%,#4a4440 40%,#5e5650 70%,#3a3532 100%);opacity:.85}
.hero-shade{position:absolute;inset:0;background:rgba(0,0,0,.35)}
.hero-content{position:absolute;left:0;width:1200px;top:80px;text-align:center;color:var(--white)}
.hero-title{font-size:56px;font-weight:300;letter-spacing:2px;text-transform:uppercase;line-height:66px}
.hero-text{font-size:20px;font-weight:600;text-transform:uppercase;line-height:28px;margin:16px auto 0;width:900px}
.hero-more{display:inline-block;margin-top:20px;border:1px solid var(--white);font-size:12px;font-weight:700;padding:6px 14px}

/* about */
.about{top:530px;left:150px;width:900px;height:310px;background:var(--white);box-shadow:0 0 14px rgba(0,0,0,.15);text-align:center;padding:28px 70px}
.heading{font-size:24px;font-weight:400;text-transform:uppercase;letter-spacing:1px;color:var(--ink);text-align:center}
.heading b{color:var(--orange);font-weight:400}
.heading-rule{width:60px;height:2px;background:var(--orange);margin:8px auto 18px}
.about p{font-size:13px;line-height:22px;color:var(--muted);margin-bottom:14px}

/* services */
.services{top:870px;height:360px}
.service-row{position:absolute;top:72px;left:150px;width:900px;display:flex;gap:25px}
.service{width:283px}
.service-img{height:180px}
.service-img.legal{background:linear-gradient(135deg,#c2a58a,#6b4e3a)}
.service-img.finance{background:linear-gradient(135deg,#e0e0e0,#9a9a9a)}
.service-img.health{background:linear-gradient(135deg,#d6d6d6,#7d7d7d)}
.service-label{margin-top:10px;height:36px;line-height:34px;text-align:center;font-size:12px;text-transform:uppercase;color:var(--muted);border:1px solid var(--line)}
.service.current .service-img{outline:3px solid var(--orange)}
.service.current .service-label{color:var(--orange);border-color:var(--orange)}
.arrow{position:absolute;top:150px}

/* news & blog */
.updates{top:1240px;height:210px;background:var(--band)}
.col-head{position:absolute;top:22px;font-size:22px;text-transform:uppercase}
.col-head b{color:var(--orange);font-weight:400}
.news-item{position:absolute;top:70px;width:150px}
.news-date{color:var(--orange);font-size:12px;font-weight:700;border-bottom:1px solid #cfcfcf;padding-bottom:6px}
.news-title{font-size:13px;font-weight:700;margin-top:8px}
.news-text{font-size:11px;color:var(--muted);line-height:16px;margin-top:4px}
.news-more{font-size:11px;color:var(--orange);margin-top:6px}
.blog-item{position:absolute;top:70px;width:150px}
.blog-thumb{width:64px;height:64px;background:linear-gradient(135deg,#c9c9c9,#8a8a8a);border:2px solid var(--white)}
.blog-text{font-size:11px;color:var(--muted);line-height:16px;margin-top:10px}
.divider{position:absolute;left:680px;top:20px;width:1px;height:170px;background:#cfcfcf}

/* partners */
.partners{top:1470px;height:180px}
.partner-row{position:absolute;top:80px;left:170px;width:860px;display:flex;justify-content:space-between;align-items:center}
.partner{height:26px;width:110px}
.partner.red{background:var(--partner-red);opacity:.8}
.partner.grey{background:var(--partner-grey);opacity:.6}
.partner.blue{background:var(--partner-blue);opacity:.75;width:130px}
.partner.square{width:60px;height:60px;background:var(--partner-grey);opacity:.45}

/* testimonials */
.testimonials{top:1660px;height:330px;background:linear-gradient(180deg,#4a4746,#3b3938);color:var(--white)}
.testimonials .heading{color:var(--white);padding-top:26px}
.quote{position:absolute;top:100px;left:220px;width:760px;text-align:center;font-size:15px;line-height:24px}
.quote-by{font-size:16px;font-weight:700;margin-top:10px}
.dots{position:absolute;top:240px;left:0;width:1200px;display:flex;justify-content:center;gap:8px}
.dots span{width:10px;height:10px;border-radius:50%;background:#888}
.dots span.on{background:var(--white)}
.client{position:absolute;width:46px;height:46px;background:#6a6664}

/* footer */
.footer{top:1990px;height:240px;background:var(--white);border-top:4px solid var(--orange)}
.foot-col{position:absolute;top:26px}
.foot-col h4{font-size:14px;font-weight:700;color:var(--orange);text-transform:uppercase;margin-bottom:14px}
.foot-col li{list-style:none;font-size:12px;color:var(--muted);line-height:22px}
.foot-col li::before{content:"› ";color:var(--orange)}
.contact-line{font-size:12px;color:var(--muted);line-height:18px;margin-bottom:8px}
.contact-line b{color:var(--orange);font-weight:600;display:block}
.field{border:1px solid var(--line);height:32px;font-size:12px;color:#aaa;padding:7px 10px}
.send{background:var(--orange);color:var(--white);text-align:center;font-size:13px;font-weight:700;height:34px;line-height:34px;margin-top:8px}
.bottom-bar{top:2230px;height:50px;background:#f4f4f4;border-top:1px solid var(--line)}
.copyright{position:absolute;left:72px;top:16px;font-size:12px;color:var(--muted)}
.social{position:absolute;right:72px;top:12px;display:flex;gap:6px}
.social span{width:26px;height:26px;background:#9a9a9a}
.social span.on{background:var(--orange)}
</style>
</head>
<body>

<header class="section site-header">
  <div class="brand">
    <div class="brand-name">TROBANEX</div>
    <div class="brand-sub"><span class="dot"></span>TRANSLATIONS</div>
  </div>
  <nav class="nav">
    <a class="active">Home</a><a>About Us</a><a>Services</a><a>Language</a><a>Blog</a><a>Contact Us</a>
  </nav>
  <div class="header-actions">
    <span class="btn upload-login"><svg width="12" height="12" viewBox="0 0 12 12" aria-hidden="true"><path d="M6 9V1M2.5 4.5L6 1l3.5 3.5M1 11h10" fill="none" stroke="#fff" stroke-width="1.6"/></svg>Trobanex Login</span>
    <span class="btn">Sign Up Now</span>
  </div>
</header>

<section class="section hero">
  <div class="hero-photo" role="img" aria-label="Group of business people in suits standing together"></div>
  <div class="hero-shade"></div>
  <div class="hero-content">
    <h1 class="hero-title">Professional Translators</h1>
    <p class="hero-text">Lorem ipsum dolor sit amet, consectetur adipiscing elit. Nullam vehicul nisi vitae euismod gravida. Nam egestas turp</p>
    <span class="hero-more">LEARN MORE</span>
  </div>
</section>

<section class="section about">
  <h2 class="heading">About <b>Trobanex</b></h2>
  <div class="heading-rule"></div>
  <p>Lorem ipsum dolor sit amet, consectetur adipiscing elit. Nullam vehicula nisi vitae euismod gravida. Nam egestas turpis quis neque volutpat, sed fermentum lorem porta. Cras dictum ante sed porttitor finibus. Curabitur sodales tellus, facilisis vitae felis non, dignissim ultrices lectus.</p>
  <p>Nulla sagittis, enim a mollis malesuada, leo tortor facilisis orci, eget volutpat magna dui sed est. Sed eget sapien nibh, non pellentesque nisi sollicitudin lacinia. Ut lobortis porttitor mauris, et tempus mi pharetra ac.</p>
</section>

<section class="section services">
  <h2 class="heading">Our <b>Services</b></h2>
  <div class="heading-rule"></div>
  <svg class="arrow" style="left:116px" width="20" height="30" viewBox="0 0 20 30"><path d="M15 3 L5 15 L15 27" fill="none" stroke="#bbb" stroke-width="3"/></svg>
  <div class="service-row">
    <div class="service current">
      <div class="service-img legal" role="img" aria-label="Gavel and law books on a desk"></div>
      <div class="service-label">Legal Translations</div>
    </div>
    <div class="service">
      <div class="service-img finance" role="img" aria-label="Stack of banknotes"></div>
      <div class="service-label">Financial Translations</div>
    </div>
    <div class="service">
      <div class="service-img health" role="img" aria-label="Doctor with stethoscope"></div>
      <div class="service-label">Healthcare Translations</div>
    </div>
  </div>
  <svg class="arrow" style="left:1064px" width="20" height="30" viewBox="0 0 20 30"><path d="M5 3 L15 15 L5 27" fill="none" stroke="#bbb" stroke-width="3"/></svg>
</section>

<section class="section updates">
  <h3 class="col-head" style="left:150px">Latest <b>News</b></h3>
  <div class="news-item" style="left:150px">
    <div class="news-date">09. 08. 2014</div>
    <div class="news-title">News Coverage And</div>
    <div class="news-text">Lorem ipsum dolor sit amet consectetur elit</div>
    <div class="news-more">Read more</div>
  </div>
  <div class="news-item" style="left:330px">
    <div class="news-date">09. 08. 2014</div>
    <div class="news-title">News Coverage And</div>
    <div class="news-text">Lorem ipsum dolor sit amet consectetur elit</div>
  </div>
  <div class="news-item" style="left:510px">
    <div class="news-date">09. 08. 2014</div>
    <div class="news-title">News Coverage And</div>
    <div class="news-text">Lorem ipsum dolor sit amet consectetur elit</div>
    <div class="news-more">Read more</div>
  </div>
  <div class="divider"></div>
  <h3 class="col-head" style="left:720px">Latest <b>Blog</b></h3>
  <div class="blog-item" style="left:720px">
    <div class="blog-thumb" role="img" aria-label="Blog author portrait"></div>
    <div class="blog-text">Lorem ipsum dolor sit amet consectetur elit</div>
  </div>
  <div class="blog-item" style="left:880px">
    <div class="blog-thumb" role="img" aria-label="Blog author portrait"></div>
    <div class="blog-text">Lorem ipsum dolor sit amet consectetur elit</div>
  </div>
</section>

<section class="section partners">
  <h2 class="heading">Our <b>Partners</b></h2>
  <div class="heading-rule"></div>
  <div class="partner-row">
    <div class="partner red" role="img" aria-label="Partner badge"></div>
    <div class="partner grey" role="img" aria-label="Partner badge"></div>
    <div class="partner square" role="img" aria-label="Partner badge"></div>
    <div class="partner blue" role="img" aria-label="Partner badge"></div>
    <div class="partner grey" role="img" aria-label="Partner badge"></div>
  </div>
</section>

<section class="section testimonials" role="img" aria-label="Background collage of client portraits">
  <h2 class="heading">What our happy clients say</h2>
  <div class="heading-rule"></div>
  <div class="client" style="left:90px;top:70px"></div>
  <div class="client" style="left:160px;top:190px"></div>
  <div class="client" style="left:1000px;top:80px"></div>
  <div class="client" style="left:1080px;top:200px"></div>
  <div class="quote">
    Lorem ipsum dolor sit amet, consectetur adipiscing elit. Sed sed purus sit amet dui fermentum nec. Duis vel nisi metus, fermentum nisi enim, tempor eget risus vel. Sed mollis nulla.
    <div class="quote-by">Lorem ipsum dolor sit amet</div>
  </div>
  <div class="dots"><span class="on"></span><span></span><span></span></div>
</section>

<footer class="section footer">
  <div class="foot-col" style="left:150px">
    <h4>Trobanex</h4>
    <ul><li>Home</li><li>About Us</li><li>Services</li><li>Language</li><li>Blog</li><li>Contact Us</li></ul>
  </div>
  <div class="foot-col" style="left:380px;width:220px">
    <h4>Contact Us</h4>
    <div class="contact-line"><b>Address:</b>1234 Harbour Street, Suite 500, Anytown</div>
    <div class="contact-line"><b>Phone No:</b>+1 555 0142 / +1 555 0187</div>
    <div class="contact-line"><b>Email Id:</b>info@trobanextranslations.com</div>
  </div>
  <div class="foot-col" style="left:680px;width:370px">
    <h4>Contact Form</h4>
    <div style="display:flex;gap:8px;margin-bottom:8px"><div class="field" style="flex:1">Name</div><div class="field" style="flex:1">Email</div></div>
    <div class="field" style="height:70px">Message</div>
    <div class="send">SEND MESSAGE</div>
  </div>
</footer>

<div class="section bottom-bar">
  <div class="copyright">© 2014 Trobanex. All rights reserved.</div>
  <div class="social"><span class="on"></span><span></span><span></span><span></span><span></span></div>
</div>

</body>
</html>
```